依頼詳細
❏デザイン依頼
・テ−マカラ−:黄緑。おだやか系の頂点。さわやかやあたらしい気持ちなどの意味がある
・作りたいイメ−ジ:とても明るく、幸せを感じる体質つくりのお手伝い。
会いたいとおもってもらう雰囲気

☆リッチメニューのデザインの狙い
・人柄を全面にだし、講座への参加の流れをつくる。

❏依頼詳細
<作成物>
■リッチメッセージ
リッチメニュー
合計2枚

〈リッチメニューの項目〉
下の段左から右へ①〜③
下の段左から右へ④〜⑤

〈リッチメニューの表示名〉
①自己紹介/HP/SNS ②講座のご案内   ③お客様の声
④なるほど情報   ⑤お楽しみ     ⑥予約・問い合わせ

デザイン重視でここの表示名はデザイン的に英語の方がよければ
英語でも大丈夫です。意味がわかって
ニュアンスがあっていれば文字を短くするのも
お任せします。あくまでデザイン重視です。

〈画像はこちらから〉
↓ソラボックスリンク
https://7.sorabox-dl.jp/0422-a3f1e9b07d52c846e0d3a71f5b92c684

※こちらの作成以外に勝手に使用された場合は
著作権侵害で法的手段をとらせていただきます。
作成事例にもしようしないでください。

<サイズ>
・リッチメッセージ(1040×1040ピクセル)
・リッチメニュー(1200×810ピクセル)

<納品形式>
・ai形式(イラストレーターデータ)
・JPG
記載項目
キャッチコピ−
自分力発見ナビゲ−タ−
サイズ
• ・リッチメッセージ(1040×1040ピクセル) ・リッチメニュー(1200×810ピクセル)
希望イメージ
シンプル 複雑
単色 カラフル
暗い 明るい
日常 高級
遊び心 厳粛
未来的 伝統的
女性的 男性的
希望する色
黄・オレンジ系、緑系
納品ファイル
• 高解像度JPG (.jpg)
• イラストレーター形式 (.ai)
補足説明
■ 選んだ理由

依頼にフィットした提案でした。

■ 提案者全員のお礼・コメント

様々な素敵な提案ありがとうございました。
次回も是非ご応募ください。

```html
<!DOCTYPE html>
<html lang="ja">
<head>
<meta charset="utf-8">
<title>自分力発見ナビゲーター リッチメニュー</title>
<link rel="stylesheet" href="https://fonts.googleapis.com/css2?family=M+PLUS+Rounded+1c:wght@500;700;800&display=swap">
<style>
  :root {
    --bg: #fbf8d2;
    --green: #8cc63e;
    --green-dark: #5a9e1f;
    --green-light: #b5dc7d;
    --red: #e8423a;
    --yellow: #f5d21c;
    --blue: #2c8fd6;
    --lime: #7cc242;
    --white: #ffffff;
    --text-green: #2f8a2a;
  }
  * { box-sizing: border-box; margin: 0; padding: 0; }
  html, body { width: 706px; height: 1200px; overflow: hidden; }
  body {
    background: var(--bg);
    font-family: "M PLUS Rounded 1c", sans-serif;
    position: relative;
  }
  .title-banner {
    position: absolute; left: 71px; top: 19px; width: 564px; height: 64px;
    background: var(--green); border-radius: 14px;
    color: var(--white); font-weight: 800; font-size: 44px;
    display: flex; align-items: center; justify-content: center; letter-spacing: 2px;
  }
  .portrait {
    position: absolute; left: 0; top: 100px; width: 330px; height: 560px;
    background: linear-gradient(180deg, #f3e3cf 0%, #f5a25a 55%, #f08a3a 100%);
    border-radius: 0 40% 0 0;
  }
  .photo-circle {
    position: absolute; border-radius: 50%; border: 8px solid;
    background: linear-gradient(160deg, #e9e4dc, #b9a99a);
  }
  .photo-circle.red { left: 290px; top: 112px; width: 198px; height: 198px; border-color: var(--red); }
  .photo-circle.yellow { left: 484px; top: 108px; width: 188px; height: 188px; border-color: var(--yellow); }
  .photo-circle.lime { left: 282px; top: 462px; width: 188px; height: 188px; border-color: var(--lime); background: linear-gradient(160deg, #cfe3b8, #6f9a58); }
  .photo-circle.blue { left: 506px; top: 462px; width: 188px; height: 188px; border-color: var(--blue); background: linear-gradient(160deg, #dfe6ee, #8aa0b6); }
  .pointers { position: absolute; left: 0; top: 0; }
  .message-box {
    position: absolute; left: 304px; top: 332px; width: 392px; height: 116px;
    background: var(--white); border: 5px solid var(--green);
    color: var(--text-green); font-weight: 800; font-size: 34px; line-height: 1.3;
    display: flex; flex-direction: column; align-items: center; justify-content: center;
  }
  .instructor {
    position: absolute; left: 14px; top: 598px; color: var(--text-green); font-weight: 700;
  }
  .instructor .role { font-size: 19px; line-height: 1.3; }
  .instructor .name { font-size: 32px; font-weight: 800; margin-top: 2px; }
  .menu {
    position: absolute; left: 19px; top: 725px; width: 670px; height: 463px;
    display: grid; grid-template-columns: repeat(3, 1fr); grid-template-rows: repeat(2, 1fr);
    column-gap: 24px; row-gap: 24px;
  }
  .menu-tile {
    background: var(--green); border: 4px solid var(--green-light); border-radius: 10px;
    display: flex; flex-direction: column; align-items: center; justify-content: center;
    color: var(--white); font-weight: 700; font-size: 22px; text-align: center; line-height: 1.25;
  }
  .menu-tile svg { width: 96px; height: 96px; margin-bottom: 10px; }
</style>
</head>
<body>
  <div class="title-banner">自分力発見ナビゲーター</div>

  <div class="portrait" role="img" aria-label="オレンジのスカーフを巻いた講師の写真"></div>

  <svg class="pointers" width="706" height="720" aria-hidden="true">
    <polygon points="372,306 404,306 388,334" fill="var(--red)"/>
    <polygon points="560,292 592,292 576,334" fill="var(--yellow)"/>
    <polygon points="360,462 392,462 376,448" fill="var(--lime)"/>
    <polygon points="584,462 616,462 600,448" fill="var(--blue)"/>
  </svg>

  <div class="photo-circle red" role="img" aria-label="講座で話す講師の写真"></div>
  <div class="photo-circle yellow" role="img" aria-label="パソコンの前で説明する講師の写真"></div>
  <div class="photo-circle lime" role="img" aria-label="屋外で子どもたちと活動する写真"></div>
  <div class="photo-circle blue" role="img" aria-label="グループ講座の様子の写真"></div>

  <div class="message-box">
    <span>色（=個性）で</span>
    <span>輝ける人のお手伝い!</span>
  </div>

  <div class="instructor">
    <p class="role">いろどりタイプ<br>インストラクター認定講師</p>
    <p class="name">森川あかり</p>
  </div>

  <nav class="menu">
    <div class="menu-tile">
      <svg viewBox="0 0 96 96" aria-hidden="true"><path d="M48 10 L90 50 H78 V86 H58 V62 H38 V86 H18 V50 H6 Z" fill="#fff"/></svg>
      <span>自己紹介<br>HP/SNS</span>
    </div>
    <div class="menu-tile">
      <svg viewBox="0 0 96 96" aria-hidden="true"><rect x="14" y="8" width="54" height="76" rx="4" fill="#fff"/><g stroke="var(--green)" stroke-width="4"><line x1="24" y1="26" x2="58" y2="26"/><line x1="24" y1="40" x2="58" y2="40"/><line x1="24" y1="54" x2="46" y2="54"/></g><path d="M82 30 L90 38 L56 72 L44 76 L48 64 Z" fill="#fff" stroke="var(--green)" stroke-width="3"/></svg>
      <span>講座のご案内</span>
    </div>
    <div class="menu-tile">
      <svg viewBox="0 0 96 96" aria-hidden="true"><path d="M8 14 H62 V50 H30 L18 62 V50 H8 Z" fill="#fff"/><g fill="var(--green)"><circle cx="22" cy="32" r="4"/><circle cx="35" cy="32" r="4"/><circle cx="48" cy="32" r="4"/></g><path d="M40 42 H88 V74 H80 V86 L68 74 H40 Z" fill="#fff" stroke="var(--green)" stroke-width="3"/><g fill="var(--green)"><circle cx="54" cy="58" r="4"/><circle cx="65" cy="58" r="4"/><circle cx="76" cy="58" r="4"/></g></svg>
      <span>お客様の声</span>
    </div>
    <div class="menu-tile">
      <svg viewBox="0 0 96 96" aria-hidden="true"><path d="M48 10 C30 10 22 24 22 36 C22 50 34 56 36 66 H60 C62 56 74 50 74 36 C74 24 66 10 48 10 Z" fill="#fff"/><rect x="36" y="70" width="24" height="6" rx="2" fill="#fff"/><rect x="38" y="80" width="20" height="6" rx="3" fill="#fff"/><path d="M48 56 V34 M40 34 H56" stroke="var(--green)" stroke-width="4" fill="none"/></svg>
      <span>なるほど情報</span>
    </div>
    <div class="menu-tile">
      <svg viewBox="0 0 96 96" aria-hidden="true"><rect x="12" y="34" width="72" height="16" fill="#fff"/><rect x="18" y="52" width="60" height="36" fill="#fff"/><rect x="44" y="34" width="8" height="54" fill="var(--green)"/><path d="M48 34 C36 14 22 20 30 32 Z M48 34 C60 14 74 20 66 32 Z" fill="none" stroke="#fff" stroke-width="5"/></svg>
      <span>お楽しみ</span>
    </div>
    <div class="menu-tile">
      <svg viewBox="0 0 96 96" aria-hidden="true"><rect x="8" y="22" width="80" height="54" fill="none" stroke="#fff" stroke-width="5"/><path d="M8 22 L48 54 L88 22" fill="none" stroke="#fff" stroke-width="5"/></svg>
      <span>予約・問い合わせ</span>
    </div>
  </nav>
</body>
</html>
```